Fernquill Stationary Design
The Ledger Desk Firm
Fernquill Stationary Design -
Creative Brief
Professional
Marla Dempton
3847 W. Harlan Pkwy. Suite 410 Irving, TX 75061
mdempton@fernquill.example
www.fernquill.example
We want to be different in our space. Most if not all of our competitors have boring, text-intensive websites. We want to be different. We're agile, nimple, quick, crisp, entrepreneurial, hip/cool.
Logo, Tagline (The Ledger Desk Firm) and our website address (www.fernquill.example) At the end of the day, play around with what looks cool!

```html
<!DOCTYPE html>
<html lang="en">
<head>
<meta charset="utf-8">
<title>Fernquill Stationery</title>
<link rel="stylesheet" href="https://fonts.googleapis.com/css2?family=Arimo:wght@400;700&display=swap">
<style>
  :root {
    --stage: #1b1b1b;
    --stage-edge: #0c0c0c;
    --green: #7cc242;
    --green-soft: #a7d97a;
    --ink: #2b2b2b;
    --muted: #6a6a6a;
    --paper-top: #ffffff;
    --paper-bottom: #d9d9d9;
    --night: #0d0d0d;
    --white: #ffffff;
  }
  * { box-sizing: border-box; margin: 0; padding: 0; }
  html, body { width: 1200px; height: 370px; overflow: hidden; }
  body {
    font-family: "Arimo", Arial, sans-serif;
    background: radial-gradient(ellipse at center, var(--stage) 0%, var(--stage-edge) 100%);
    position: relative;
  }
  .card {
    position: absolute;
    top: 12px;
    width: 564px;
    height: 336px;
    overflow: hidden;
    box-shadow: 0 4px 14px rgba(0,0,0,.6);
  }
  .card--front {
    left: 24px;
    background: linear-gradient(180deg, var(--paper-top) 0%, var(--paper-bottom) 100%);
  }
  .card--back {
    left: 612px;
    background: var(--night);
    border: 1px solid #333;
  }
  .hero-figure {
    position: absolute;
    left: 40px;
    top: 30px;
    width: 290px;
    height: 306px;
    border-radius: 46% 54% 40% 30% / 30% 36% 64% 70%;
    background: radial-gradient(ellipse at 45% 55%, var(--green) 0%, var(--green-soft) 100%);
  }
  .brand {
    position: absolute;
    display: flex;
    flex-direction: column;
    align-items: center;
  }
  .brand__dot {
    border-radius: 50%;
    background: var(--green);
  }
  .brand__name {
    font-weight: 700;
    letter-spacing: 1px;
    line-height: 1;
  }
  .brand__tagline {
    text-transform: uppercase;
    letter-spacing: 1.5px;
    line-height: 1;
  }
  .card--front .brand { left: 36px; top: 40px; align-items: flex-start; }
  .card--front .brand__dot { width: 48px; height: 48px; margin: 0 0 64px 22px; }
  .card--front .brand__name { font-size: 40px; color: var(--ink); }
  .card--front .brand__tagline { font-size: 10px; color: var(--ink); margin-top: 5px; }

  .contact {
    position: absolute;
    left: 336px;
    top: 38px;
    color: var(--ink);
  }
  .contact__name { font-size: 19px; margin-bottom: 52px; }
  .contact__address { font-style: normal; font-size: 13px; line-height: 19px; margin-left: 36px; }
  .contact__lines { list-style: none; margin: 58px 0 0 22px; font-size: 12.5px; line-height: 22px; }
  .contact__lines span { display: inline-block; width: 18px; color: var(--muted); }

  .card--back .brand { left: 0; right: 0; top: 40px; }
  .card--back .brand__dot { width: 82px; height: 82px; margin-bottom: 40px; }
  .card--back .brand__name { font-size: 58px; color: var(--white); letter-spacing: 2px; }
  .card--back .brand__tagline { font-size: 12px; color: var(--white); margin-top: 10px; letter-spacing: 3px; }
  .card--back .web {
    position: absolute;
    left: 0; right: 0;
    top: 278px;
    text-align: center;
    font-size: 13px;
    color: var(--white);
  }
</style>
</head>
<body>
  <section class="card card--front">
    <div class="hero-figure" role="img" aria-label="Large green leaping hare silhouette"></div>
    <div class="brand">
      <span class="brand__dot"></span>
      <span class="brand__name">FERNQUILL</span>
      <span class="brand__tagline">The Ledger Desk Firm</span>
    </div>
    <div class="contact">
      <p class="contact__name">Marla Dempton</p>
      <address class="contact__address">
        3847 W. Harlan Pkwy.<br>
        Suite 410<br>
        Irving, TX 75061
      </address>
      <ul class="contact__lines">
        <li><span>P</span>: 972-555-0142</li>
        <li><span>C</span>: 214-555-0187</li>
        <li><span>F</span>: 800-555-0163</li>
        <li><span>E</span>: mdempton@fernquill.example</li>
        <li><span>W</span>: www.fernquill.example</li>
      </ul>
    </div>
  </section>

  <section class="card card--back">
    <div class="brand">
      <span class="brand__dot"></span>
      <span class="brand__name">FERNQUILL</span>
      <span class="brand__tagline">The Ledger Desk Firm</span>
    </div>
    <p class="web">www.fernquill.example</p>
  </section>
</body>
</html>
```